Business Card Design Project

Business Card
We are rebranding with a new logo
Industry/Entity Type
Business
Contact Information for Business Card
Dennis Marlow +61 427581962 dennis@qovo.com.au P.O. Box 872 Kelvindale QLD 4309
Requirements
Must have
- Logo

```html
<!DOCTYPE html>
<html lang="en">
<head>
<meta charset="utf-8">
<title>Qovo – Business Card</title>
<link rel="stylesheet" href="https://fonts.googleapis.com/css2?family=Lato:wght@400;700&display=swap">
<style>
  :root {
    --backdrop: #4a4a4c;
    --card-black: #050505;
    --card-blue-top: #22a6df;
    --card-blue-bottom: #0b6e9c;
    --accent-orange: #f39322;
    --text-white: #ffffff;
    --icon-blue: #1b8fc6;
  }
  * { margin: 0; padding: 0; box-sizing: border-box; }
  html, body {
    width: 1200px;
    height: 926px;
    overflow: hidden;
    background: var(--backdrop);
    font-family: "Lato", Arial, sans-serif;
  }
  .canvas {
    position: relative;
    width: 1200px;
    height: 926px;
  }
  .business-card {
    position: absolute;
    left: 150px;
    top: 206px;
    width: 900px;
    height: 514px;
    overflow: hidden;
    background: linear-gradient(180deg, var(--card-blue-top) 0%, var(--card-blue-bottom) 100%);
    box-shadow: 0 18px 40px rgba(0,0,0,0.35);
  }
  .card-shapes {
    position: absolute;
    inset: 0;
    width: 900px;
    height: 514px;
  }
  .shape-black { fill: var(--card-black); }
  .shape-orange { fill: var(--accent-orange); }
  .company-name {
    position: absolute;
    left: 60px;
    top: 64px;
    display: flex;
    align-items: center;
    gap: 12px;
    color: var(--text-white);
    font-weight: 400;
    font-size: 40px;
    line-height: 1;
  }
  .company-dot {
    width: 14px;
    height: 14px;
    border-radius: 50%;
    background: var(--accent-orange);
  }
  .contact-block {
    position: absolute;
    right: 58px;
    top: 262px;
    text-align: right;
    color: var(--text-white);
  }
  .person-name {
    font-size: 36px;
    font-weight: 400;
    letter-spacing: 1px;
    margin-bottom: 30px;
  }
  .person-name .surname { font-weight: 700; }
  .contact-list { list-style: none; }
  .contact-item {
    display: flex;
    justify-content: flex-end;
    align-items: center;
    gap: 12px;
    font-size: 23px;
    letter-spacing: 0.5px;
    height: 34px;
  }
  .contact-icon {
    width: 28px;
    height: 28px;
    background: var(--text-white);
    border-right: 4px solid var(--accent-orange);
    border-bottom: 3px solid var(--accent-orange);
    display: flex;
    align-items: center;
    justify-content: center;
  }
  .contact-icon svg { width: 18px; height: 18px; fill: var(--icon-blue); }
</style>
</head>
<body>
<div class="canvas">
  <div class="business-card">
    <svg class="card-shapes" viewBox="0 0 900 514" aria-hidden="true">
      <path class="shape-orange" d="M0 395 C180 380 330 320 430 240 C350 330 190 410 0 434 Z"/>
      <path class="shape-black" d="M0 0 H560 C470 190 290 370 0 405 Z"/>
    </svg>

    <div class="company-name"><span class="company-dot"></span><span>Qovo</span></div>

    <div class="contact-block">
      <p class="person-name">DENNIS <span class="surname">MARLOW</span></p>
      <ul class="contact-list">
        <li class="contact-item">
          <span>+61 427581962</span>
          <span class="contact-icon"><svg viewBox="0 0 24 24"><path d="M6.6 10.8a15.2 15.2 0 0 0 6.6 6.6l2.2-2.2c.3-.3.7-.4 1-.2 1.1.4 2.3.6 3.6.6.6 0 1 .4 1 1V20c0 .6-.4 1-1 1A17 17 0 0 1 3 4c0-.6.4-1 1-1h3.5c.6 0 1 .4 1 1 0 1.3.2 2.5.6 3.6.1.3 0 .7-.2 1l-2.3 2.2z"/></svg></span>
        </li>
        <li class="contact-item">
          <span>dennis@qovo.com.au</span>
          <span class="contact-icon"><svg viewBox="0 0 24 24"><path d="M2 5h20v14H2z M4 7v.4l8 5.2 8-5.2V7z" fill-rule="evenodd"/></svg></span>
        </li>
        <li class="contact-item">
          <span>P.O. Box 872 Kelvindale QLD 4309</span>
          <span class="contact-icon"><svg viewBox="0 0 24 24"><path d="M12 2a7 7 0 0 0-7 7c0 5.2 7 13 7 13s7-7.8 7-13a7 7 0 0 0-7-7zm0 9.5A2.5 2.5 0 1 1 12 6.5a2.5 2.5 0 0 1 0 5z"/></svg></span>
        </li>
      </ul>
    </div>
  </div>
</div>
</body>
</html>
```